BrovaLT BIZ Card, email signature & Stationary

Professional business cards, email signatures and ms word letterhead

Target Market(s)

business owners

Industry/Entity Type

cloud hosting

Contact Information for Business Card

name title office phone number , direct line, fax email address web site

Font styles to use
Other font styles liked:
• something that compliments font in logo

```html
<!DOCTYPE html>
<html lang="en">
<head>
<meta charset="UTF-8">
<title>BrovaLT Business Card</title>
<link rel="stylesheet" href="https://fonts.googleapis.com/css2?family=Poppins:wght@300;400;500;700&display=swap">
<style>
  :root {
    --stage: #262626;
    --card-dark: #050505;
    --card-light: #ffffff;
    --brand-red: #e3141b;
    --ink: #111111;
    --paper-text: #f2f2f2;
  }
  * { margin: 0; padding: 0; box-sizing: border-box; }
  html, body {
    width: 1200px; height: 1200px; overflow: hidden;
    background: var(--stage);
    font-family: "Poppins", sans-serif;
  }
  .canvas {
    width: 1200px; height: 1200px;
    display: flex; flex-direction: column; align-items: center; justify-content: center;
    gap: 44px;
  }
  .card {
    width: 900px; height: 514px;
    position: relative;
    box-shadow: 0 14px 34px rgba(0,0,0,0.45);
  }

  /* Back side */
  .card-back {
    background: var(--card-dark);
    display: flex; flex-direction: column; align-items: center; justify-content: center;
  }
  .brand-name {
    font-weight: 400;
    color: var(--brand-red);
    line-height: 1;
    letter-spacing: 1px;
  }
  .card-back .brand-name { font-size: 118px; }
  .web-address {
    margin-top: 34px;
    color: var(--paper-text);
    font-size: 19px;
    font-weight: 500;
    letter-spacing: 7px;
  }

  /* Front side */
  .card-front {
    background: var(--card-light);
    display: flex; align-items: center;
  }
  .brand-block {
    width: 470px;
    display: flex; justify-content: center;
  }
  .card-front .brand-name { font-size: 90px; }
  .divider {
    width: 2px; height: 230px;
    background: var(--brand-red);
  }
  .contact-block {
    padding-left: 56px;
    color: var(--ink);
  }
  .person-name {
    font-size: 30px; font-weight: 700;
    letter-spacing: 1.5px; text-transform: uppercase;
    line-height: 1.1;
  }
  .person-title {
    font-size: 17px; font-weight: 400;
    color: var(--brand-red);
    letter-spacing: 1px;
  }
  .title-rule {
    width: 84px; height: 3px;
    background: var(--brand-red);
    margin: 14px 0 22px;
  }
  .contact-list { list-style: none; }
  .contact-item {
    display: flex; align-items: center; gap: 14px;
    font-size: 22px; font-weight: 400;
    line-height: 1.5;
  }
  .contact-icon { width: 26px; height: 26px; flex: none; }
</style>
</head>
<body>
<main class="canvas">
  <section class="card card-back">
    <div class="brand-name">BrovaLT</div>
    <div class="web-address">www.brovaltcloud.com</div>
  </section>

  <section class="card card-front">
    <div class="brand-block">
      <div class="brand-name">BrovaLT</div>
    </div>
    <div class="divider"></div>
    <div class="contact-block">
      <div class="person-name">Marcus T Lindell</div>
      <div class="person-title">CEO</div>
      <div class="title-rule"></div>
      <ul class="contact-list">
        <li class="contact-item">
          <svg class="contact-icon" viewBox="0 0 26 26" aria-hidden="true">
            <circle cx="13" cy="13" r="13" fill="#e3141b"/>
            <path d="M9 7.5c.6-.5 1.3-.4 1.7.2l1.1 1.8c.3.5.2 1.1-.2 1.5l-.7.6c.6 1.4 1.6 2.5 3 3.1l.6-.7c.4-.4 1-.5 1.5-.2l1.8 1.1c.6.4.7 1.1.2 1.7l-.8.9c-.8.8-2 1-3 .5-2.8-1.4-4.8-3.5-6.1-6.2-.5-1-.3-2.2.5-3z" fill="#fff"/>
          </svg>
          <span>(555) 014-2290</span>
        </li>
        <li class="contact-item">
          <svg class="contact-icon" viewBox="0 0 26 26" aria-hidden="true">
            <circle cx="13" cy="13" r="13" fill="#e3141b"/>
            <rect x="9" y="6.5" width="8" height="13" rx="1.4" fill="none" stroke="#fff" stroke-width="1.6"/>
            <circle cx="13" cy="17" r="0.9" fill="#fff"/>
          </svg>
          <span>(555) 014-2290</span>
        </li>
        <li class="contact-item">
          <svg class="contact-icon" viewBox="0 0 26 26" aria-hidden="true">
            <circle cx="13" cy="13" r="13" fill="#e3141b"/>
            <rect x="9.5" y="6.5" width="7" height="4" fill="#fff"/>
            <rect x="7" y="11" width="12" height="6" rx="1" fill="#fff"/>
            <rect x="9.5" y="15" width="7" height="4.5" fill="#fff" stroke="#e3141b" stroke-width="0.8"/>
          </svg>
          <span>(555) 014-2290</span>
        </li>
        <li class="contact-item">
          <svg class="contact-icon" viewBox="0 0 26 26" aria-hidden="true">
            <circle cx="13" cy="13" r="13" fill="#e3141b"/>
            <rect x="7" y="8.5" width="12" height="9" rx="1" fill="#fff"/>
            <path d="M7.5 9l5.5 4.5L18.5 9" fill="none" stroke="#e3141b" stroke-width="1.2"/>
          </svg>
          <span>info@brovaltmail.com</span>
        </li>
      </ul>
    </div>
  </section>
</main>
</body>
</html>
```